Gourmet Restaurant take out menu

We need a take out menu design that is trendy for a casual upscale Italian restaurant with a vast menu. This menu must be able to be 4 color and reproducible in large quantities to be bulked mailed or inserted into a daily paper. It must also maintain a theme that can be crossed over to our in house dining menu and specials menu.
OUR WEBSITE:
www.velmorabistrohouse.example
For the content, go to the Menu section of our website. We are interested in the design scheme and a template to use.
Target Market(s)
families, sinle individuals seeking take out meals and delivery
Industry/Entity Type
Restaurant

```html
<!DOCTYPE html>
<html lang="en">
<head>
<meta charset="utf-8">
<title>Velmora Bistro House – Take Out Menu</title>
<link href="https://fonts.googleapis.com/css2?family=Cinzel:wght@400;700&family=Source+Sans+3:ital,wght@0,400;1,800&display=swap" rel="stylesheet">
<style>
:root{
  --orange:#f07c1b;
  --orange-soft:#f6a65c;
  --wine:#8b1a10;
  --ink:#3a3a3a;
  --paper:#ffffff;
  --shadow:rgba(0,0,0,.22);
}
*{box-sizing:border-box;margin:0;padding:0}
html,body{width:1200px;height:794px;overflow:hidden;background:var(--paper)}
body{font-family:"Source Sans 3",Arial,sans-serif;color:var(--ink)}
ul{list-style:none}
.menu{position:relative;width:1200px;height:794px;background:var(--paper)}
.frame-line{position:absolute;height:2px;background:var(--orange-soft)}
.frame-line.top{top:18px;left:90px;right:90px}
.frame-line.bottom{bottom:26px;left:90px;right:90px}
.frame-side{position:absolute;top:40px;bottom:60px;width:0;border-left:2px dotted var(--orange)}
.frame-side.left{left:14px}.frame-side.right{right:14px}

.cover{position:absolute;left:38px;top:36px;width:354px;height:708px;background:var(--paper);box-shadow:2px 3px 8px var(--shadow)}
.cover-photo{position:absolute;left:12px;top:28px;width:329px;height:260px;
  background:radial-gradient(circle at 40% 45%,#c9873f 0%,#8a4a1e 45%,#3a1f10 100%)}
.brand{position:absolute;left:0;right:0;top:345px;text-align:center;color:var(--wine);font-family:"Cinzel",serif;font-weight:400;font-size:31px;line-height:1.15;letter-spacing:1px}
.contact{position:absolute;left:0;right:0;text-align:center;color:var(--wine);font-family:"Cinzel",serif;line-height:1.05}
.contact h3{font-weight:700;font-size:15px}
.contact p{font-size:15.5px}
.contact.call{top:482px}.contact.visit{top:526px}.contact.hours{top:582px}
.contact.hours p{font-size:15px;margin-bottom:12px}

.col-rule{position:absolute;top:36px;bottom:56px;border-left:2px dotted var(--orange)}

.col{position:absolute;top:48px}
.col.pizza{left:424px;width:356px}
.col.side{left:814px;width:356px;top:0;height:794px}
.heading{display:flex;align-items:center;gap:10px;color:var(--orange);font-weight:800;font-style:italic;font-size:21px;line-height:24px;white-space:nowrap}
.heading::before,.heading::after{content:"";flex:1;height:2px;background:var(--orange)}
.item-name{color:var(--orange);font-size:10px;text-transform:uppercase;line-height:14.2px}
.desc{font-size:10px;line-height:14.2px}
.pizza .inner{padding-left:10px}
.pizza .item{margin-top:14px}
.toppings{margin-top:10px}
.sizes{font-size:10px;line-height:14.2px;margin-top:10px}
.side .section{position:absolute;left:0;right:0}
.hot{top:48px}.cold{top:252px}.burgers-sec{top:374px}
.note{text-align:center;font-size:10px;margin:6px 0 6px}
.subs{display:grid;grid-template-columns:181px 1fr;font-size:10px;line-height:14.2px;padding-left:11px}
.burgers{padding-left:11px;margin-top:14px}
.burgers .item{margin-top:14px}
.burgers .item:first-child{margin-top:0}
</style>
</head>
<body>
<main class="menu">
  <div class="frame-line top"></div>
  <div class="frame-line bottom"></div>
  <div class="frame-side left"></div>
  <div class="frame-side right"></div>

  <section class="cover">
    <div class="cover-photo" role="img" aria-label="Close-up photo of a pepperoni and olive pizza with melted cheese"></div>
    <div class="brand">Velmora<br>Bistro House</div>
    <div class="contact call"><h3>Call us at</h3><p>555-014-2276</p></div>
    <div class="contact visit"><h3>Visit us at</h3><p>118 Larkmoor Avenue, Brightwater, NJ</p></div>
    <div class="contact hours">
      <h3>Hours:</h3>
      <p>Dining Room: Mon-Thu 11am – 11pm,<br>Fri-Sat 11am – 12am, Sun 12pm – 11pm</p>
      <p>Takeout: Mon-Thu 11am – 10pm, Fri-Sat<br>11am – 11pm, Sun 12pm – 10pm</p>
    </div>
  </section>

  <section class="col pizza">
    <h2 class="heading">Gourmet Pizza</h2>
    <div class="inner">
      <div class="toppings">
        <div class="item-name">Toppings for 1.99</div>
        <p class="desc">HAM • BROCCOLI • EXTRA CHEESE • TOMATOES HOT OR SWEET PEPPERS • ROASTED PEPPERS • PEPPERONI • SPINACH • ITALIAN SAUSAGE • BLACK OLIVES • GREEN PEPPERS • MUSHROOMS • ONIONS • ANCHOVIES • GRILLED CHICKEN • MEATBALL BACON and RICOTTA 3.00</p>
      </div>
      <p class="sizes">10" Individual, 12" Medium, 16" Large &nbsp;•&nbsp; Pizza By The Slice - Plain 1.99, Veggie 2.99</p>
      <div class="item"><div class="item-name">Plain Cheese .... 8.99/11.99/12.99</div></div>
      <div class="item"><div class="item-name">Traditional White .... 8.59/11.59/13.99</div><p class="desc">Olive oil, garlic, mozzarella cheese</p></div>
      <div class="item"><div class="item-name">Chicken Pacon Ranch ...10.99/14.99/16.99</div><p class="desc">Garlic chicken, bacon, pepperjack and cheddar cheese, red onions, diced tomatoes, drizzle of ranch dressing</p></div>
      <div class="item"><div class="item-name">Bronx Bomber ... 11.99/14.99/16.99</div><p class="desc">Sausage, prosciutto ham, oregano, crumbled bleu and mozzarella cheese</p></div>
      <div class="item"><div class="item-name">Buffalo Chicken ... 10.99/14.99/16.99</div><p class="desc">Buffalo sauce, chicken, mozzarella cheese, side of bleu cheese dressing</p></div>
      <div class="item"><div class="item-name">Gourmet Special ... 12.99/16.99/18.99</div><p class="desc">Pepperoni, sausage, bell peppers, mushrooms, onion, mozzarella cheese</p></div>
      <div class="item"><div class="item-name">Margarita ... 8.99/11.99/13.99</div><p class="desc">Fresh basil, tomato, buffalo mozzarella cheese</p></div>
      <div class="item"><div class="item-name">Roasted Vegetable ... 11.99/14.99/16.99</div><p class="desc">Eggplant, red and yellow peppers, onions, artichokes, Kalamata olives, tomatoes, mozzarella cheese. Veggie Lover Olive oil, garlic, broccoli, spinach, tomato, mozzarella cheese.</p></div>
      <div class="item"><div class="item-name">Sweet Hawaiian ... 11.99/14.99/16.99</div><p class="desc">Pineapple, tomatoes, ham, mozzarella cheese.</p></div>
      <div class="item"><div class="item-name">Spinach and Artichoke ... 8.99/11.99/12.99</div><p class="desc">Spinach, artichoke hearts, basil, mozzarella, parmesan cheese.</p></div>
      <div class="item"><div class="item-name">Philly Cheese Steak ... 11.99/14.99/16.99</div><p class="desc">Philly steak, green peppers, onions, provolone, American cheese.</p></div>
      <div class="item"><div class="item-name">Grandma's Pie ... 14.99</div><p class="desc">Thin crust pizza topped with mozzarella, tomato sauce, buffalo mozzarella, fresh basil, olive oil. (One Size)</p></div>
    </div>
  </section>

  <div class="col-rule" style="left:796px"></div>

  <section class="col side">
    <div class="section hot">
      <h2 class="heading">Hot Subs</h2>
      <p class="note">add cheese for 0.59</p>
      <div class="subs">
        <ul>
          <li>Cheesesteak ...6.59</li><li>Bacon Cheesesteak ... 7.59</li><li>Steak Sub ... 6.29</li><li>Chicken Parmigiana ... 6.99</li><li>Pepper, Egg, &amp; Cheese ... 6.29</li><li>Pizza Cheesesteak ... 6.99</li><li>Meatball Parmigiana ... 6.99</li><li>Mushroom Cheesesteak ... 6.99</li><li>Veal Parmigiana ... 7.99</li><li>Pepper Cheesesteak ... 6.99</li>
        </ul>
        <ul>
          <li>Vegetarian with Cheese ... 6.59</li><li>Eggplant Parmigiana ... 6.59</li><li>Chicken Cheesesteak ... 6.99</li><li>Sausage Parmigiana ... 7.59</li><li>Grilled Chicken ... 6.59</li><li>Cheeseburger Sub ... 7.59</li><li>Chicken Cacciatore ... 7.59</li><li>Steak Cacciatore ... 7.59</li><li>Sausage, Peppers, &amp; Onion ... 6.99</li>
        </ul>
      </div>
    </div>
    <div class="section cold">
      <h2 class="heading">Cold Subs</h2>
      <p class="note">add cheese for 0.59</p>
      <div class="subs">
        <ul>
          <li>Regular Italian ... 6.59</li><li>Tuna ... 6.59</li><li>Roast Beef ... 7.59</li><li>Imported Ham ... 6.59</li>
        </ul>
        <ul style="padding-top:3px">
          <li>Roast Turkey ... 6.99</li><li>Provolone ... 6.59</li><li>Capicola, Salami, &amp; Provolone ... 6.99</li><li>Chicken Salad ... 6.99</li>
        </ul>
      </div>
    </div>
    <div class="section burgers-sec">
      <h2 class="heading">Awesome burgers</h2>
      <div class="burgers">
        <div class="item"><div class="item-name">Cheeseburger ... 7.99</div></div>
        <div class="item"><div class="item-name">Bacon Cheddar ... 8.99</div><p class="desc">Applewood smoked bacon, sharp cheddar</p></div>
        <div class="item"><div class="item-name">Blue Cheese BLT ... 9.59</div><p class="desc">Bacon, lettuce, tomato, onion, mayonnaise, bleu cheese</p></div>
        <div class="item"><div class="item-name">California... 9.99</div><p class="desc">Avocado, roasted green chilies, pepper jack cheese, chipotle mayo, ranch dressing</p></div>
        <div class="item"><div class="item-name">Gourmet Sliders... 8.99</div><p class="desc">5 bite-sized burgers with American cheese on mini potato rolls</p></div>
        <div class="item"><div class="item-name">Mushroom Swiss ... 8.59</div><p class="desc">Sautéed mushrooms, onions and mayo topped with Swiss cheese</p></div>
        <div class="item"><div class="item-name">Portabella .. 8.59</div><p class="desc">Angus burger, roasted portabella, melted provolone cheese</p></div>
        <div class="item"><div class="item-name">Pub ... 9.99</div><p class="desc">House steak sauce and mayo, topped with onion rings, bleu cheese.</p></div>
      </div>
    </div>
  </section>
</main>
</body>
</html>
```